TEK Logistics - Banner 2.5' x 8' for 20+ locations

Need a banner designed that will pop. This banner will be displayed at over 20 of our transportation facilities. Goal is for the banner to grab the attention of employees, contractors and clients and help reinforce our mission and core values. Designed needs to include TEK Logo, our core values and mission statement. Red and Black are the main company colors and we need to stay within that theme and color pallet. Attached is a previous version that was too basic and boring. Willing to consider a design that excludes the mission statement.

Gathering more feedback

```html
<!DOCTYPE html>
<html lang="en">
<head>
<meta charset="utf-8">
<title>TEK Logistics – Core Values Banner</title>
<link rel="stylesheet" href="https://fonts.googleapis.com/css2?family=Open+Sans:wdth,wght@75,600;75,700&display=swap">
<style>
  :root {
    --page-bg: #e6e9ed;
    --banner-light: #ffffff;
    --banner-grey: #d2d2d4;
    --ink: #262533;
    --brand-red: #d4212a;
    --swoosh-red: #f2393f;
    --band-dark: #2a2934;
  }
  * { margin: 0; padding: 0; box-sizing: border-box; }
  html, body {
    width: 1200px;
    height: 889px;
    overflow: hidden;
    background: var(--page-bg);
  }
  .banner {
    position: absolute;
    left: 30px;
    top: 238px;
    width: 1140px;
    height: 413px;
    overflow: hidden;
    background: linear-gradient(90deg, var(--banner-light) 0%, var(--banner-light) 42%, var(--banner-grey) 100%);
    box-shadow: 0 2px 10px rgba(0,0,0,0.15);
  }
  .banner__waves {
    position: absolute;
    inset: 0;
    width: 100%;
    height: 100%;
  }
  .brand {
    position: absolute;
    left: 60px;
    top: 108px;
    display: flex;
    align-items: center;
    gap: 14px;
    font-family: "Open Sans", "Arial Narrow", sans-serif;
    font-stretch: 75%;
    font-weight: 700;
    color: var(--ink);
  }
  .brand__dot {
    width: 22px;
    height: 22px;
    border-radius: 50%;
    background: var(--brand-red);
    flex: none;
  }
  .brand__name {
    display: flex;
    flex-direction: column;
    line-height: 0.95;
  }
  .brand__name-main { font-size: 72px; letter-spacing: 2px; }
  .brand__name-sub { font-size: 30px; letter-spacing: 6px; }
  .values {
    list-style: none;
    position: absolute;
    right: 52px;
    top: 38px;
    font-family: "Open Sans", "Arial Narrow", sans-serif;
    font-stretch: 75%;
    font-weight: 700;
    text-align: right;
    color: var(--ink);
  }
  .values__item {
    display: flex;
    justify-content: flex-end;
    align-items: center;
    gap: 8px;
    font-size: 36px;
    line-height: 55.5px;
    height: 55.5px;
  }
  .values__tick {
    width: 22px;
    height: 20px;
    flex: none;
  }
  .values__motto {
    font-size: 29px;
    line-height: 44px;
    color: var(--brand-red);
    font-weight: 600;
  }
  .values__bullet { margin: 0 5px; }
</style>
</head>
<body>
  <section class="banner" aria-label="TEK Logistics core values banner">
    <svg class="banner__waves" viewBox="0 0 1740 630" preserveAspectRatio="none" aria-hidden="true">
      <path fill="var(--swoosh-red)" d="M0,360 C450,500 950,548 1340,528 L1740,420 L1740,630 L0,630 Z"/>
      <path fill="var(--band-dark)" d="M0,455 C520,600 1150,640 1740,425 L1740,630 L0,630 Z"/>
    </svg>

    <div class="brand">
      <span class="brand__dot"></span>
      <span class="brand__name">
        <span class="brand__name-main">TEK</span>
        <span class="brand__name-sub">LOGISTICS</span>
      </span>
    </div>

    <ul class="values">
      <li class="values__item">
        <svg class="values__tick" viewBox="0 0 22 20" aria-hidden="true"><path d="M2,11 L8,17 L20,3" fill="none" stroke="var(--ink)" stroke-width="3"/></svg>
        DO THE RIGHT THINGS FOR THE RIGHT PERSONS
      </li>
      <li class="values__item">
        <svg class="values__tick" viewBox="0 0 22 20" aria-hidden="true"><path d="M2,11 L8,17 L20,3" fill="none" stroke="var(--ink)" stroke-width="3"/></svg>
        PERSUE GROWTH AND DEVLOPMENT
      </li>
      <li class="values__item">
        <svg class="values__tick" viewBox="0 0 22 20" aria-hidden="true"><path d="M2,11 L8,17 L20,3" fill="none" stroke="var(--ink)" stroke-width="3"/></svg>
        BUILD A POSITIVE TEAM ATMOSPHERE
      </li>
      <li class="values__item">
        <svg class="values__tick" viewBox="0 0 22 20" aria-hidden="true"><path d="M2,11 L8,17 L20,3" fill="none" stroke="var(--ink)" stroke-width="3"/></svg>
        DELIVER WOW THROUGH SERVICE
      </li>
      <li class="values__motto">
        <span class="values__bullet">•</span>DO EVERYTHING SAFELY<span class="values__bullet">•</span>HAVE FUN
      </li>
    </ul>
  </section>
</body>
</html>
```